Professional DJ Business Card

Business card for giving out to clubs and venues or interested groups that are in need of a professional DJ. I want something artistic and catchy/alluring, with a minimalist approach that gets just the vital amount of info and leaves the rest for inquiry via contacting me. Ideally I would like one side to have an image of something cool like an eye and my name, then the other side be the contact info, I am definitely feeling a black or dark colored card, but I am open to other designs. I am uploading a picture that I made that reflects a little of what I am *kind of* looking for.

Industry/Entity Type

Business

Contact Information for Business Card

Tomas Halvik (Voxtel)
Professional DJ (West Coast)
EDM (Deep/House/Techno), Hip Hop, Latin, Trap.
Cell: 555-274-9163
Email: Voxtelofficial@mailnest.net
www.beatcloudia.net/yourtuneisfading

```html
<!DOCTYPE html>
<html lang="en">
<head>
<meta charset="utf-8">
<title>Voxtel – Professional DJ Business Card</title>
<link rel="stylesheet" href="https://fonts.googleapis.com/css2?family=Arimo:wght@400;700&display=swap">
<style>
  :root {
    --stage: #e6e4df;
    --card-dark: #161a18;
    --card-dark-2: #0c0e0d;
    --ink-light: #f2f2f2;
    --ink-soft: #d6d6d6;
    --swoosh-grey: #9a9a9a;
    --swoosh-white: #ffffff;
    --swoosh-black: #0a0a0a;
  }
  * { margin: 0; padding: 0; box-sizing: border-box; }
  html, body {
    width: 1200px; height: 950px; overflow: hidden;
    background: var(--stage);
    font-family: "Arimo", Arial, sans-serif;
  }
  .stage {
    width: 1200px; height: 950px;
    display: flex; flex-direction: column; align-items: center; justify-content: center;
    gap: 50px;
  }
  .card {
    position: relative;
    width: 700px; height: 400px;
    background: linear-gradient(135deg, var(--card-dark) 0%, var(--card-dark-2) 100%);
    box-shadow: 0 10px 28px rgba(0,0,0,.28);
    overflow: hidden;
    color: var(--ink-light);
  }

  /* Front */
  .card-front { display: flex; align-items: center; justify-content: center; }
  .brand { display: flex; align-items: center; gap: 14px; }
  .brand-dot {
    width: 22px; height: 22px; border-radius: 50%;
    background: var(--ink-light);
  }
  .brand-name {
    font-weight: 700; font-size: 64px; letter-spacing: 1px; color: var(--ink-light);
  }

  /* Back */
  .swoosh { position: absolute; inset: 0; width: 100%; height: 100%; }
  .back-brand { position: absolute; left: 58px; top: 92px; }
  .back-brand .brand-name { font-size: 40px; }
  .back-brand .brand-dot { width: 14px; height: 14px; }
  .genres {
    position: absolute; left: 58px; top: 178px;
    font-size: 17px; line-height: 24px; color: var(--ink-light);
  }
  .contacts {
    position: absolute; left: 58px; top: 248px;
    list-style: none; font-size: 17px; line-height: 28px; color: var(--ink-light);
  }
  .contacts li { display: flex; align-items: center; gap: 10px; }
  .contacts svg { width: 16px; height: 16px; flex: none; }
  .identity {
    position: absolute; left: 420px; top: 96px;
  }
  .identity-name { font-weight: 700; font-size: 20px; color: var(--ink-light); }
  .identity-role { font-size: 16px; margin-top: 6px; color: var(--ink-soft); }
</style>
</head>
<body>
<main class="stage">

  <section class="card card-front" aria-label="Card front">
    <div class="brand">
      <span class="brand-dot"></span>
      <span class="brand-name">Voxtel</span>
    </div>
  </section>

  <section class="card card-back" aria-label="Card back">
    <svg class="swoosh" viewBox="0 0 700 400" preserveAspectRatio="none" aria-hidden="true">
      <path d="M230 400 C420 360 560 300 700 200 L700 400 Z" fill="var(--swoosh-grey)"/>
      <path d="M250 400 C430 368 570 312 700 222 L700 400 Z" fill="var(--swoosh-black)"/>
      <path d="M280 400 C450 376 590 322 700 250 L700 400 Z" fill="var(--swoosh-grey)"/>
      <path d="M300 400 C470 384 600 334 700 268 L700 400 Z" fill="var(--swoosh-white)"/>
    </svg>

    <div class="brand back-brand">
      <span class="brand-dot"></span>
      <span class="brand-name">Voxtel</span>
    </div>

    <p class="genres">EDM (Deep/House/Techno)<br>Hip Hop, Latin, Trap.</p>

    <ul class="contacts">
      <li>
        <svg viewBox="0 0 16 16"><rect x="4" y="1" width="8" height="14" rx="1.5" fill="none" stroke="var(--ink-light)" stroke-width="1.6"/><circle cx="8" cy="12.5" r="0.9" fill="var(--ink-light)"/></svg>
        555-274-9163
      </li>
      <li>
        <svg viewBox="0 0 16 16"><rect x="1" y="3.5" width="14" height="9" fill="var(--ink-light)"/><path d="M1 3.5 L8 9 L15 3.5" fill="none" stroke="var(--card-dark)" stroke-width="1.3"/></svg>
        Voxtelofficial@mailnest.net
      </li>
      <li>
        <svg viewBox="0 0 16 16"><circle cx="8" cy="8" r="6" fill="var(--ink-light)"/></svg>
        www.beatcloudia.net/yourtuneisfading
      </li>
    </ul>

    <div class="identity">
      <p class="identity-name">Tomas Halvik (Voxtel)</p>
      <p class="identity-role">Professional DJ (West Coast)</p>
    </div>
  </section>

</main>
</body>
</html>
```